Tot Petal Product Label for Tear-Free Head-to-Toe Wash

Need a bottle label design for a new line of natural products targeting infants and children. Products are Pediatrician-developed and paraben-free, sulfate-free, fragrance-free, and cruelty-free. Design should be clean and have a high-end feel to it. Will need other product labels in Tot Petal line designed as well in upcoming projects.

Target Market(s)

Newborn to young elementary age children and their parents

Industry/Entity Type

Cosmetics/Beauty

Font styles to use
Other font styles liked:
• Brand fonts are Jost and Sonorous

Colors

Designer to choose colors to be used in the design.

Requirements
Must have
• Tot Petal logo, Pediatrician Developed logo, and a clean high-end feel to it. The label must fit the specialty bottle we will be using (label measurements and diagram will be provided) for the front and back of bottle only (NOT the side labels). It must include our list of ingredients (will provide once designer selected).
Nice to have
• Should stand out on the shelf of other baby products due to it's clean simplicity and high-end feel
Should not have
• too much of a "kiddie" feel to it (targeting the parents not the kids)

```html
<!DOCTYPE html>
<html lang="en">
<head>
<meta charset="utf-8">
<title>Tot Petal – Head-to-Toe Wash Label</title>
<link rel="stylesheet" href="https://fonts.googleapis.com/css2?family=Jost:wght@300;400;500&family=Fredoka:wght@600&display=swap">
<style>
  :root {
    --page-bg: #eef1f2;
    --label-white: #ffffff;
    --sky: #93e7fb;
    --ring: #e3ecfa;
    --ink: #1c1c1c;
    --mark-ink: #2a2a2a;
  }
  html, body {
    margin: 0;
    width: 1200px;
    height: 1200px;
    overflow: hidden;
    background: var(--page-bg);
  }
  .canvas {
    position: relative;
    width: 1200px;
    height: 1200px;
  }
  .label {
    position: absolute;
    left: 252px;
    top: 100px;
    width: 695px;
    height: 1000px;
    display: block;
  }
  .label-body { fill: var(--label-white); }
  .hero-disc { fill: var(--sky); }
  .hero-ring { fill: none; stroke: var(--ring); stroke-width: 8; stroke-linecap: round; }
  .eyebrow {
    font-family: "Jost", sans-serif;
    font-weight: 300;
    font-size: 14px;
    fill: var(--label-white);
    letter-spacing: 0.2px;
  }
  .product-name {
    font-family: "Fredoka", sans-serif;
    font-weight: 600;
    fill: var(--label-white);
    letter-spacing: -1px;
  }
  .claims {
    font-family: "Jost", sans-serif;
    font-weight: 300;
    font-size: 14.5px;
    fill: var(--label-white);
    letter-spacing: 0.3px;
  }
  .claim-bullet { fill: none; stroke: var(--label-white); stroke-width: 1.1; }
  .certification-badge { fill: var(--label-white); stroke: var(--mark-ink); stroke-width: 1.2; }
  .brand-mark-circle { fill: none; stroke: var(--mark-ink); stroke-width: 1.2; }
  .brand-mark-name {
    font-family: "Jost", sans-serif;
    font-weight: 500;
    font-size: 11px;
    fill: var(--mark-ink);
    letter-spacing: 1px;
  }
  .fine-print {
    font-family: "Jost", sans-serif;
    font-weight: 400;
    font-size: 8.6px;
    fill: var(--ink);
  }
  .volume {
    font-family: "Jost", sans-serif;
    font-weight: 400;
    font-size: 14px;
    fill: var(--ink);
  }
</style>
</head>
<body>
<main class="canvas">
  <svg class="label" viewBox="725 1015 483 695" xmlns="http://www.w3.org/2000/svg" aria-label="Tot Petal Head-to-Toe Wash front label">
    <defs>
      <clipPath id="label-shape">
        <path d="M725,1710 V1115 Q725,1062 780,1045 Q870,1015 965,1015 Q1060,1015 1150,1045 Q1208,1064 1208,1122 V1710 Z"/>
      </clipPath>
    </defs>

    <path class="label-body" d="M725,1710 V1115 Q725,1062 780,1045 Q870,1015 965,1015 Q1060,1015 1150,1045 Q1208,1064 1208,1122 V1710 Z"/>

    <g class="brand-mark">
      <circle class="brand-mark-circle" cx="965" cy="1090" r="9"/>
      <text class="brand-mark-name" x="965" y="1122" text-anchor="middle">TOT PETAL</text>
    </g>

    <g clip-path="url(#label-shape)">
      <path class="hero-ring" d="M750,1182 A237,237 0 1 1 722,1572"/>
      <circle class="hero-disc" cx="878" cy="1384" r="214"/>
    </g>

    <text class="eyebrow" x="772" y="1271">Pediatrician Developed</text>
    <circle class="certification-badge" cx="993" cy="1264" r="24"/>

    <text class="product-name" x="770" y="1348" font-size="76">TOT</text>
    <text class="product-name" x="770" y="1430" font-size="76">PETAL</text>

    <g class="claims">
      <circle class="claim-bullet" cx="849" cy="1476" r="3.2"/>
      <text x="858" y="1481">PARABEN-FREE</text>
      <circle class="claim-bullet" cx="849" cy="1497" r="3.2"/>
      <text x="858" y="1502">SULFATE-FREE</text>
      <circle class="claim-bullet" cx="849" cy="1517" r="3.2"/>
      <text x="858" y="1522">FRAGRANCE-FREE</text>
      <circle class="claim-bullet" cx="849" cy="1538" r="3.2"/>
      <text x="858" y="1543">CRUELTY-FREE</text>
    </g>

    <text class="fine-print" x="773" y="1660">Lorem ipsum dolor sit amet, consectetur adipiscing elit.</text>
    <text class="fine-print" x="773" y="1672">Nunc viverra orci in massa congue, at vulputate elit posuere.</text>
    <text class="volume" x="1137" y="1669">75ml</text>
  </svg>
</main>
</body>
</html>
```